Lose Up To 1 LB Of Fat Per Day

We need a double sided street sign for our weight loss clinic. We need the doctors picture to the right side of the sign and we need a challenge “Lose Up To 1 Pound Of Fat Per Day” included in the signage.
Our color scheme for the clinic are black, white, teal and silver.
The phone number should be at the bottom of the sign
555-206–3948

Target Market(s)

Weight Loss

Font styles to use
Sans Serif

```html
<!DOCTYPE html>
<html lang="en">
<head>
<meta charset="utf-8">
<title>Lose Up To A Pound Of Fat Per Day – Street Sign</title>
<link href="https://fonts.googleapis.com/css2?family=Montserrat:wght@700;800&display=swap" rel="stylesheet">
<style>
  :root {
    --page-bg: #dcdcdc;
    --teal-light: #1fa6a7;
    --teal-dark: #067370;
    --gold: #efd48b;
    --white: #f3f3f3;
    --band: #f2f2f2;
    --purple: #4a3670;
    --suit: #1f1f22;
    --skin: #c99a80;
  }
  * { margin: 0; padding: 0; box-sizing: border-box; }
  html, body {
    width: 1200px;
    height: 864px;
    overflow: hidden;
    background: var(--page-bg);
  }
  .sign {
    position: absolute;
    left: 20px;
    top: 142px;
    width: 1160px;
    height: 580px;
    overflow: hidden;
    font-family: "Montserrat", Arial, sans-serif;
  }
  .sign__hero {
    position: absolute;
    left: 0; top: 0;
    width: 100%;
    height: 381px;
    background: radial-gradient(ellipse 520px 420px at 830px 190px, var(--teal-light), var(--teal-dark) 100%);
  }
  .sign__contact-band {
    position: absolute;
    left: 0; top: 381px;
    width: 100%;
    height: 199px;
    background: var(--band);
  }
  .doctor-photo {
    position: absolute;
    right: 21px;
    top: 26px;
    width: 420px;
    height: 554px;
    border-radius: 120px 120px 0 0;
    background: linear-gradient(180deg, var(--skin) 0%, var(--skin) 40%, var(--suit) 46%, #2a2a2e 100%);
  }
  .headline-group,
  .phone {
    position: absolute;
    left: 28px;
    width: 690px;
    text-align: center;
  }
  .headline {
    position: absolute;
    left: 0;
    width: 100%;
    font-weight: 700;
    line-height: 1;
    color: var(--white);
    letter-spacing: 1px;
    white-space: nowrap;
  }
  .headline-group { top: 0; height: 381px; }
  .headline--lose { top: 46px; font-size: 134px; }
  .headline--pound { top: 198px; font-size: 48px; color: var(--gold); }
  .headline--day { top: 269px; font-size: 72px; }
  .phone {
    top: 440px;
    font-weight: 800;
    font-size: 76px;
    line-height: 1;
    color: var(--purple);
    letter-spacing: 1px;
    white-space: nowrap;
  }
</style>
</head>
<body>
  <div class="sign">
    <div class="sign__hero"></div>
    <div class="sign__contact-band"></div>
    <div class="headline-group">
      <div class="headline headline--lose">LOSE</div>
      <div class="headline headline--pound">UP TO A POUND OF FAT</div>
      <div class="headline headline--day">PER DAY</div>
    </div>
    <div class="phone"># 555 206 3948</div>
    <div class="doctor-photo" role="img" aria-label="Photo of the clinic doctor in a dark suit and purple tie"></div>
  </div>
</body>
</html>
```